Daily Care Record Sheets

As a preschool, we have notes that we send home on a daily basis so the parents know what is going on. We would like to reformat the preschool and toddler sheets<br/><br/>The preschool participation sheet is 4.25"x 5.6"<br/>We have attached an example of what we are using currently and the information we would like on our new sheet. We would like the logo added as well.<br/><br/>The Little Sprouts sheet should be a half page. I have included 2 examples as well as a sheet of what we would like on it moving forward. <br/><br/>Please do not hesitate to reach out if you have any questions on any of this. They will print in black and white on colored paper.<br/><br/>Thanks!<br/>Marla

Target Market(s)

Parents of the toddlers and preschools in our care

Industry/Entity Type

Preschool

Colors

Designer to choose only greyscale colors for use in the design.

Requirements
Must have
• Logo
• The items in the "FOR NEW VERSION" files

```html
<!DOCTYPE html>
<html lang="en">
<head>
<meta charset="utf-8">
<title>Preschool Participation Sheet</title>
<link href="https://fonts.googleapis.com/css2?family=Cinzel:wght@700&family=Crimson+Text:wght@400;700&family=Roboto:wght@400&display=swap" rel="stylesheet">
<style>
  :root {
    --page-bg: #e6e4e0;
    --card-bg: #ffffff;
    --ink: #2a2a2a;
    --title-ink: #4a1114;
    --rule: #333333;
    --brick-red: #e8242a;
    --brick-blue: #1f6fe0;
    --brick-lightblue: #3eb3f0;
    --brick-green: #5cbc1e;
    --brick-pink: #f04fb4;
    --brick-purple: #9b3fe6;
    --brick-orange: #ff8a12;
    --brick-yellow: #ffcc14;
    --brick-black: #3a3a3a;
    --brand-ink: #111111;
  }
  html, body {
    margin: 0;
    width: 1200px;
    height: 1200px;
    overflow: hidden;
    background: var(--page-bg);
  }
  .sheet {
    position: absolute;
    left: 80px;
    top: 205px;
    width: 1040px;
    height: 790px;
    background: var(--card-bg);
    box-shadow: 0 4px 18px rgba(0,0,0,.18);
  }
  .sheet-border { position: absolute; inset: 0; }
  .sheet-title {
    position: absolute;
    left: 110px;
    top: 96px;
    width: 600px;
    margin: 0;
    font-family: "Cinzel", serif;
    font-weight: 700;
    font-size: 31px;
    line-height: 40px;
    letter-spacing: 0.5px;
    text-transform: uppercase;
    white-space: nowrap;
    color: var(--title-ink);
  }
  .title-rule {
    position: absolute;
    left: 110px;
    top: 150px;
    width: 560px;
    border-top: 1.5px solid var(--rule);
  }
  .record-fields {
    position: absolute;
    left: 110px;
    top: 178px;
    width: 540px;
    font-family: "Crimson Text", serif;
    font-size: 24px;
    line-height: 1.25;
    color: var(--ink);
  }
  .field { margin: 0 0 16px; white-space: nowrap; }
  .field-label { font-weight: 700; }
  .fill-line {
    display: inline-block;
    vertical-align: bottom;
    border-bottom: 1.5px solid var(--rule);
    height: 22px;
  }
  .lunch-options span + span { margin-left: 18px; }
  .kids-illustration {
    position: absolute;
    left: 670px;
    top: 120px;
    width: 280px;
    height: 320px;
    border-radius: 40% 40% 30% 30%;
    background: radial-gradient(circle at 50% 45%, #f3c9a1 0%, #c98a55 45%, #8a5a3a 75%, rgba(255,255,255,0) 100%);
  }
  .brand {
    position: absolute;
    right: 92px;
    top: 560px;
    display: flex;
    align-items: center;
    gap: 10px;
    font-family: "Roboto", sans-serif;
    font-size: 27px;
    white-space: nowrap;
    color: var(--brand-ink);
  }
  .brand-dot {
    width: 22px;
    height: 22px;
    border-radius: 50%;
    background: var(--brand-ink);
  }
</style>
</head>
<body>
  <article class="sheet">
    <svg class="sheet-border" width="1040" height="790" viewBox="0 0 1040 790">
      <g class="border-left">
        <rect x="0" y="0" width="58" height="113" fill="var(--brick-yellow)"/>
        <rect x="0" y="113" width="58" height="113" fill="var(--brick-red)"/>
        <rect x="0" y="226" width="58" height="113" fill="var(--brick-blue)"/>
        <rect x="0" y="339" width="58" height="113" fill="var(--brick-green)"/>
        <rect x="0" y="452" width="58" height="113" fill="var(--brick-pink)"/>
        <rect x="0" y="565" width="58" height="113" fill="var(--brick-orange)"/>
        <rect x="0" y="678" width="58" height="112" fill="var(--brick-lightblue)"/>
      </g>
      <g class="border-right">
        <rect x="982" y="0" width="58" height="113" fill="var(--brick-pink)"/>
        <rect x="982" y="113" width="58" height="113" fill="var(--brick-green)"/>
        <rect x="982" y="226" width="58" height="113" fill="var(--brick-yellow)"/>
        <rect x="982" y="339" width="58" height="113" fill="var(--brick-black)"/>
        <rect x="982" y="452" width="58" height="113" fill="var(--brick-blue)"/>
        <rect x="982" y="565" width="58" height="113" fill="var(--brick-purple)"/>
        <rect x="982" y="678" width="58" height="112" fill="var(--brick-red)"/>
      </g>
      <g class="border-top">
        <rect x="0" y="0" width="130" height="58" fill="var(--brick-purple)"/>
        <rect x="130" y="0" width="130" height="58" fill="var(--brick-pink)"/>
        <rect x="260" y="0" width="130" height="58" fill="var(--brick-green)"/>
        <rect x="390" y="0" width="130" height="58" fill="var(--brick-lightblue)"/>
        <rect x="520" y="0" width="130" height="58" fill="var(--brick-red)"/>
        <rect x="650" y="0" width="130" height="58" fill="var(--brick-black)"/>
        <rect x="780" y="0" width="130" height="58" fill="var(--brick-blue)"/>
        <rect x="910" y="0" width="130" height="58" fill="var(--brick-orange)"/>
      </g>
      <g class="border-bottom">
        <rect x="0" y="732" width="130" height="58" fill="var(--brick-purple)"/>
        <rect x="130" y="732" width="130" height="58" fill="var(--brick-orange)"/>
        <rect x="260" y="732" width="130" height="58" fill="var(--brick-blue)"/>
        <rect x="390" y="732" width="130" height="58" fill="var(--brick-red)"/>
        <rect x="520" y="732" width="130" height="58" fill="var(--brick-black)"/>
        <rect x="650" y="732" width="130" height="58" fill="var(--brick-yellow)"/>
        <rect x="780" y="732" width="130" height="58" fill="var(--brick-pink)"/>
        <rect x="910" y="732" width="130" height="58" fill="var(--brick-green)"/>
      </g>
    </svg>

    <h1 class="sheet-title">Preschool Participation</h1>
    <div class="title-rule"></div>

    <section class="record-fields">
      <p class="field">Child : <span class="fill-line" style="width:290px"></span></p>
      <p class="field">Date : <span class="fill-line" style="width:290px"></span></p>
      <p class="field lunch-options"><span class="field-label">Lunch:</span> <span>ALL</span><span>MOST</span><span>SOME</span><span>NONE</span></p>
      <p class="field"><span class="field-label">Disposition:</span> Happy / Curious / Friendly / Sleepy<br>
        Cheerful / Energetic / Quiet / Talkative<br>
        Mischievous / Followed Directions</p>
      <p class="field"><span class="field-label">Nap Time:</span><br>
        I Slept Well / I was Quiet / I didn’t feel like resting</p>
      <p class="field"><span class="field-label">Today I had fun..</span> <span class="fill-line" style="width:280px"></span></p>
      <p class="field"><span class="field-label">Notes/Reminders:</span> <span class="fill-line" style="width:270px"></span></p>
    </section>

    <div class="kids-illustration" role="img" aria-label="Cartoon illustration of a group of smiling children gathered around a wooden crate"></div>

    <div class="brand">
      <span class="brand-dot"></span>
      <span class="brand-name">Bright Steps Academy</span>
    </div>
  </article>
</body>
</html>
```